Rootline App - Static Google Ad Image

We need a static image design that promotes our website, which provides an online incident investigation collaboration tool. I would like this static image for Google, but I am also seeking the same design in a LinkedIn Ad ratio.

We would like to see engaging ad graphics that capture the essence of collaboration, time saving, fast "impact-to-learnings" type vibe. As it helps them collaborate and facilitate the investigation on our interactive canvas and then it has an automated report builder that is AI-assisted to turn their information into coherent sentences in the report, it is not fully AI generated (this is important as i feel people inherently distrust AI generated content).

This tool is aimed at safety professionals in mining, construction and oil & gas who want an easy way to facilitate investigations virtually or in person without having to use whiteboards and double handle information and that want to be able to generate a report and learnings on the same day to quickly prevent further harm.

I have included a bunch of snips of my site and features etc - please feel free to use any of them but dont be constrained by these.

Target Market(s)

Safety Professionals/ Managers in Mining, Oil & Gas & Construction

Industry/Entity Type

Mining, Oil & Gas & Construction

Font styles to use
Sans Serif

Requirements
Nice to have
• Modern, pain point focussed, visual of investigation map and or nodes
Should not have
• No em-dashes, no gimmicky language or terms

```html
<!DOCTYPE html>
<html lang="en">
<head>
<meta charset="UTF-8">
<title>Rootline – Incident Investigation Software</title>
<link rel="stylesheet" href="https://fonts.googleapis.com/css2?family=Inter:wght@400;500;600;700;800&display=swap">
<style>
  :root{
    --navy:#0f2342;
    --blue:#1273d4;
    --blue-btn:#0c6fd0;
    --muted:#8693a6;
    --panel:#f3f6fa;
    --grid:#e4e9f0;
    --orange:#f4a020;
    --white:#ffffff;
    --card-line:#dfe5ee;
    --chip-bg:#eef3fb;
  }
  *{margin:0;padding:0;box-sizing:border-box}
  html,body{width:1200px;height:628px;overflow:hidden;background:var(--panel)}
  body{font-family:"Inter",Arial,sans-serif;color:var(--navy)}
  .ad{position:relative;width:1200px;height:628px;overflow:hidden}
  .copy-panel{
    position:absolute;left:0;top:0;width:625px;height:628px;
    background-color:var(--panel);
    background-image:
      linear-gradient(var(--grid) 1px,transparent 1px),
      linear-gradient(90deg,var(--grid) 1px,transparent 1px);
    background-size:48px 48px;
  }
  .brand{position:absolute;left:62px;top:44px;display:flex;align-items:center;gap:13px}
  .brand-mark{width:30px;height:30px;border:2px solid var(--navy);border-radius:4px}
  .brand-name{font-size:19px;font-weight:600;color:var(--navy)}
  .category-pill{
    position:absolute;left:60px;top:127px;height:34px;padding:0 14px;
    display:flex;align-items:center;gap:7px;
    background:#e9edf3;border:1px solid #d7dde6;border-radius:8px;
    font-size:12px;font-weight:700;letter-spacing:.1px;color:var(--navy)
  }
  .category-pill::before{content:"";width:8px;height:8px;border-radius:50%;background:var(--blue)}
  .headline{position:absolute;left:60px;top:183px;font-size:49px;font-weight:700;line-height:57px;letter-spacing:-.5px}
  .headline .accent{color:var(--blue);display:block}
  .subhead{position:absolute;left:60px;top:311px;font-size:19px;font-weight:600;color:var(--muted)}
  .benefits{position:absolute;left:60px;top:371px;list-style:none}
  .benefits li{display:flex;align-items:center;gap:11px;height:35px;font-size:17px;font-weight:600;color:var(--navy)}
  .benefits svg{flex:none}
  .cta{
    position:absolute;left:60px;top:516px;width:214px;height:66px;border-radius:4px;
    background:var(--blue-btn);color:var(--white);font-size:18px;font-weight:600;
    display:flex;align-items:center;justify-content:center;gap:8px;text-decoration:none
  }
  .signin{position:absolute;left:298px;top:538px;display:flex;align-items:center;gap:8px;font-size:14px;font-weight:600;color:var(--blue);text-decoration:none}

  .hero-photo{
    position:absolute;left:625px;top:0;width:575px;height:628px;
    background:radial-gradient(ellipse at 30% 10%,#b88a3a 0%,#6b4a1c 35%,#2e2414 70%,#1c1a16 100%);
  }
  .profile-card{
    position:absolute;left:655px;top:182px;width:194px;height:76px;background:var(--white);
    border-radius:4px;box-shadow:0 4px 14px rgba(0,0,0,.25);padding:10px 10px
  }
  .profile-top{display:flex;gap:10px;align-items:flex-start}
  .avatar{width:27px;height:27px;border-radius:3px;background:#8c8f94}
  .profile-name{font-size:13px;font-weight:700;line-height:15px}
  .profile-id{font-size:9px;color:var(--muted)}
  .more{margin-left:auto;width:22px;height:22px;border-radius:50%;background:#eef0f3;font-size:11px;font-weight:700;text-align:center;line-height:17px}
  .chips{display:flex;gap:5px;margin-top:9px}
  .chip{font-size:7px;font-weight:500;background:var(--chip-bg);border-radius:3px;padding:3px 5px;color:var(--navy)}
  .connector{position:absolute;left:0;top:0}
  .map-card{
    position:absolute;left:740px;top:340px;width:386px;height:243px;background:var(--white);
    border-radius:6px;overflow:hidden;box-shadow:0 6px 20px rgba(0,0,0,.3);border-top:13px solid var(--blue)
  }
  .map-head{display:flex;align-items:center;height:48px;padding:0 12px 0 24px;border-bottom:1px solid var(--card-line)}
  .map-title{font-size:15px;font-weight:700;margin-left:9px}
  .map-tools{margin-left:auto;display:flex;gap:6px}
  .map-tools span{width:16px;height:16px;border-radius:3px;background:var(--blue)}
  .map-canvas{position:absolute;left:24px;top:64px}
</style>
</head>
<body>
<main class="ad">
  <section class="copy-panel">
    <div class="brand"><span class="brand-mark"></span><span class="brand-name">Rootline</span></div>
    <div class="category-pill">INCIDENT INVESTIGATION SOFTWARE</div>
    <h1 class="headline">Investigate Faster<span class="accent">Report Smarter</span></h1>
    <p class="subhead">Solve the investigation workflow</p>
    <ul class="benefits">
      <li><svg width="18" height="18" viewBox="0 0 18 18"><circle cx="9" cy="9" r="9" fill="#f4a020"/><path d="M5 9.3l2.6 2.5L13 6.5" fill="none" stroke="#fff" stroke-width="2" stroke-linecap="round" stroke-linejoin="round"/></svg>Keep every investigation visible and under control</li>
      <li><svg width="18" height="18" viewBox="0 0 18 18"><circle cx="9" cy="9" r="9" fill="#f4a020"/><path d="M5 9.3l2.6 2.5L13 6.5" fill="none" stroke="#fff" stroke-width="2" stroke-linecap="round" stroke-linejoin="round"/></svg>Guide new users from blank page to useful map fast</li>
      <li><svg width="18" height="18" viewBox="0 0 18 18"><circle cx="9" cy="9" r="9" fill="#f4a020"/><path d="M5 9.3l2.6 2.5L13 6.5" fill="none" stroke="#fff" stroke-width="2" stroke-linecap="round" stroke-linejoin="round"/></svg>Share the current picture quickly in PDF form</li>
    </ul>
    <a class="cta" href="#">Start Free Trial <svg width="14" height="12" viewBox="0 0 14 12"><path d="M1 6h11M7.5 1.5L12 6l-4.5 4.5" fill="none" stroke="#fff" stroke-width="1.8" stroke-linecap="round" stroke-linejoin="round"/></svg></a>
    <a class="signin" href="#">Sign in to your workspace <svg width="14" height="12" viewBox="0 0 14 12"><path d="M1 6h11M7.5 1.5L12 6l-4.5 4.5" fill="none" stroke="#1273d4" stroke-width="1.8" stroke-linecap="round" stroke-linejoin="round"/></svg></a>
  </section>

  <div class="hero-photo" role="img" aria-label="Two smiling safety workers in yellow hard hats reviewing site plans underground"></div>

  <svg class="connector" width="1200" height="628" aria-hidden="true">
    <path d="M748 258V292H897V340" fill="none" stroke="#e8e8e8" stroke-width="1.5" stroke-dasharray="6 4"/>
  </svg>

  <div class="profile-card">
    <div class="profile-top">
      <div class="avatar" role="img" aria-label="Profile photo"></div>
      <div><div class="profile-name">Marcus T.</div><div class="profile-id">ID: 892A-44B</div></div>
      <div class="more">···</div>
    </div>
    <div class="chips"><span class="chip">3 Associated Numbers</span><span class="chip">High Priority</span></div>
  </div>

  <div class="map-card">
    <div class="map-head">
      <svg width="18" height="20" viewBox="0 0 18 20"><rect x="1.5" y="3" width="15" height="16" rx="2" fill="none" stroke="#1273d4" stroke-width="1.6"/><rect x="5.5" y="1" width="7" height="4" rx="1" fill="#fff" stroke="#1273d4" stroke-width="1.4"/><path d="M5 10h8M5 13.5h6" stroke="#1273d4" stroke-width="1.4"/></svg>
      <span class="map-title">Investigation Map</span>
      <div class="map-tools"><span></span><span></span><span></span><span></span></div>
    </div>
    <svg class="map-canvas" width="336" height="150" viewBox="0 0 336 150" aria-label="Investigation map overview">
      <g fill="#f7f8fa" stroke="#c9cfd8" stroke-width=".8">
        <rect x="0" y="0" width="238" height="32"/>
        <rect x="244" y="0" width="40" height="100"/>
        <rect x="290" y="0" width="46" height="100"/>
        <rect x="0" y="38" width="76" height="62"/>
        <rect x="82" y="38" width="156" height="62"/>
        <rect x="0" y="106" width="72" height="36"/>
        <rect x="78" y="106" width="108" height="36"/>
        <rect x="192" y="106" width="144" height="36"/>
      </g>
      <g fill="#fff" stroke="#b9c6d8" stroke-width=".6">
        <rect x="8" y="6" width="32" height="14"/><rect x="56" y="6" width="32" height="14"/><rect x="104" y="6" width="32" height="14"/><rect x="150" y="6" width="32" height="14"/><rect x="196" y="6" width="32" height="14"/>
        <rect x="250" y="8" width="28" height="22"/><rect x="250" y="42" width="28" height="22"/><rect x="250" y="74" width="28" height="18"/>
        <rect x="296" y="8" width="34" height="22"/><rect x="296" y="42" width="34" height="22"/><rect x="296" y="74" width="34" height="18"/>
        <rect x="88" y="46" width="32" height="20"/><rect x="130" y="46" width="32" height="20"/><rect x="170" y="46" width="30" height="20"/><rect x="206" y="46" width="28" height="20"/>
        <rect x="130" y="72" width="32" height="20"/><rect x="170" y="72" width="30" height="20"/><rect x="206" y="72" width="28" height="20"/>
      </g>
      <g fill="#111"><rect x="8" y="20" width="32" height="4"/><rect x="56" y="20" width="32" height="4"/><rect x="104" y="20" width="32" height="4"/><rect x="150" y="20" width="32" height="4"/><rect x="196" y="20" width="32" height="4"/></g>
      <g fill="#f6c98a"><rect x="88" y="46" width="32" height="4"/><rect x="88" y="72" width="32" height="16"/></g>
      <g fill="#f2d35c"><rect x="130" y="46" width="32" height="4"/><rect x="170" y="46" width="30" height="4"/></g>
      <g fill="#c4b3f0"><rect x="130" y="72" width="32" height="4"/><rect x="170" y="72" width="30" height="4"/><rect x="206" y="72" width="28" height="4"/></g>
      <g fill="#5ec98a"><rect x="250" y="8" width="28" height="3"/><rect x="250" y="42" width="28" height="3"/><rect x="214" y="118" width="30" height="3"/><rect x="276" y="118" width="30" height="3"/></g>
      <g fill="#d9342b"><rect x="8" y="114" width="26" height="14"/><rect x="40" y="114" width="26" height="14"/></g>
      <g fill="#1a4fcf"><rect x="86" y="114" width="30" height="14"/><rect x="122" y="114" width="30" height="14"/><rect x="156" y="114" width="26" height="14"/></g>
      <g fill="#222"><circle cx="20" cy="52" r="6"/><circle cx="56" cy="52" r="6"/><circle cx="20" cy="80" r="6"/><circle cx="56" cy="80" r="6"/></g>
      <g fill="#fff"><circle cx="20" cy="50" r="2"/><circle cx="56" cy="50" r="2"/><circle cx="20" cy="78" r="2"/><circle cx="56" cy="78" r="2"/></g>
    </svg>
  </div>
</main>
</body>
</html>
```